Linden Medical - Flyer

We are a full service pharmacy that specializes in diabetic testing and medications. We research the patient's insurance to maximize their insurance benefit and then deliver the medications monthly directly to the patient's doorstep, for free! We save the patient, time and money every month.
We would love a flyer that we can distribute to Doctor's offices and patients that sum up our pharmacy. Emphasis on saving money, time, and getting the best quality supplies by maximizing their insurance. We want it to be eye catching, clean, and professional.
You can use our logo or feel free to make your own design.
Updates
Target Market(s)
diabetic patients wanting to save money
Industry/Entity Type
Insurance
Look and feel
Each slider illustrates characteristics of the customer's brand and the style your logo design should communicate.

```html
<!DOCTYPE html>
<html lang="en">
<head>
<meta charset="utf-8">
<title>Linden Medical – Flyer</title>
<link href="https://fonts.googleapis.com/css2?family=Arimo:ital,wght@0,400;0,700;1,700&display=swap" rel="stylesheet">
<style>
  :root{
    --green:#8dbd3e;
    --green-dark:#6e9e26;
    --green-light:#b7d77a;
    --grey-text:#4d4d4d;
    --grey-mid:#8a8a8a;
    --grey-band:#7d7d7d;
    --paper:#f7f7f7;
    --page:#e9e9e6;
    --white:#ffffff;
  }
  *{box-sizing:border-box;margin:0;padding:0}
  html,body{width:1200px;height:1000px;overflow:hidden}
  body{background:var(--page);font-family:"Arimo",Arial,sans-serif;color:var(--grey-text);position:relative}
  .flyer{position:absolute;top:130px;width:520px;height:740px;background:linear-gradient(180deg,var(--white),var(--paper));box-shadow:0 6px 18px rgba(0,0,0,.18);overflow:hidden}
  .flyer--offer{left:50px}
  .flyer--about{left:630px}
  .abs{position:absolute}
  .photo{position:absolute}
  .band{position:absolute;left:0;width:520px}

  /* offer flyer */
  .offer-headline{left:26px;top:28px;width:300px;font-size:26px;line-height:1.12;font-weight:700;color:var(--grey-text);white-space:nowrap}
  .offer-photo{left:330px;top:0;width:190px;height:215px;background:linear-gradient(160deg,#f4efe8,#e3d8cc 60%,#cfc3b6)}
  .features{left:30px;top:262px;list-style:none}
  .features li{display:flex;align-items:flex-start;gap:10px;font-size:20px;line-height:1.1;margin-bottom:12px;color:var(--grey-text)}
  .features small{display:block;font-size:18px}
  .features .pair{gap:10px}
  .tri{flex:none;width:16px;height:16px;margin-top:2px}
  .gift{left:372px;top:232px;width:132px;height:132px}
  .gift svg{width:132px;height:132px}
  .gift-text{position:absolute;inset:0;display:flex;flex-direction:column;align-items:center;justify-content:center;color:var(--white);font-weight:700;text-align:center;transform:rotate(-14deg);line-height:1.05}
  .gift-text strong{font-size:26px}
  .gift-text span{font-size:11px}
  .offer-intro{left:30px;top:436px;width:450px;font-size:15px;line-height:1.3;font-weight:700;color:var(--grey-mid)}
  .offer-steps{left:42px;top:486px;width:440px;font-size:10.5px;line-height:1.45;color:var(--grey-mid)}
  .offer-steps li{margin-bottom:2px}
  .offer-cta{left:30px;top:562px;width:340px;font-size:16px;line-height:1.3;font-weight:700;color:var(--grey-mid)}
  .brand{display:flex;align-items:center;gap:8px;color:var(--green-dark);font-weight:700;line-height:1}
  .brand-mark{width:14px;height:14px;background:var(--green)}
  .brand-name{font-size:16px;letter-spacing:1px}
  .brand-name small{display:block;font-size:9px;letter-spacing:4px;margin-top:2px}
  .offer-brand{right:26px;top:612px}

  .footer{position:absolute;left:0;bottom:0;width:520px;height:70px;background:linear-gradient(180deg,var(--green-light),var(--green));display:flex;align-items:center;justify-content:space-between;padding:0 22px;color:var(--white);font-size:13px;font-weight:700}
  .contact{display:flex;align-items:center;gap:6px}
  .contact svg{width:14px;height:14px;fill:var(--white)}

  /* about flyer */
  .about-photo{left:0;top:0;width:520px;height:380px;background:linear-gradient(180deg,#f3f3f3 0%,#ece6df 45%,#d9cfc5 100%)}
  .about-brand{right:30px;top:120px}
  .about-brand .brand-mark{width:22px;height:22px}
  .about-brand .brand-name{font-size:26px}
  .about-brand .brand-name small{font-size:12px;letter-spacing:7px}
  .free-badge{left:380px;top:322px;width:110px;height:110px;border-radius:50%;background:radial-gradient(circle at 40% 35%,var(--green-light),var(--green-dark));border:5px solid var(--white);box-shadow:0 3px 8px rgba(0,0,0,.2);display:flex;flex-direction:column;align-items:center;justify-content:center;color:var(--white);font-weight:700;transform:rotate(-14deg);line-height:1.05}
  .free-badge span{font-size:11px;letter-spacing:.5px}
  .free-badge strong{font-size:24px}
  .about-headline{left:26px;top:452px;width:270px;font-size:26px;line-height:1.1;font-weight:700;color:var(--grey-text);white-space:nowrap}
  .about-copy{left:26px;top:560px;width:262px;font-size:11px;line-height:1.45;color:var(--grey-mid)}
  .about-photo-a{left:312px;top:460px;width:190px;height:95px;background:linear-gradient(135deg,#f1ebe5,#d8ccc1);border:4px solid var(--white);box-shadow:0 2px 6px rgba(0,0,0,.15)}
  .about-photo-b{left:312px;top:565px;width:190px;height:95px;background:linear-gradient(135deg,#eef1f3,#cfd6dc);border:4px solid var(--white);box-shadow:0 2px 6px rgba(0,0,0,.15)}
</style>
</head>
<body>

<article class="flyer flyer--offer">
  <div class="photo offer-photo" role="img" aria-label="Photo of a woman peering over a sheet of paper"></div>
  <h1 class="abs offer-headline">Are the Costs of<br>your Diabetic Testing<br>supplies as high as<br>your Blood Sugar?</h1>
  <svg class="band" style="top:160px" height="100" viewBox="0 0 520 100" aria-hidden="true">
    <polygon points="0,18 520,62 520,78 0,34" fill="var(--green)"/>
    <polygon points="0,34 520,78 520,92 0,48" fill="var(--grey-band)"/>
  </svg>
  <ul class="abs features">
    <li><svg class="tri" viewBox="0 0 18 18"><polygon points="9,1 17,17 1,17" fill="var(--green)"/></svg><span>Free Meter<small>(when you qualify)</small></span></li>
    <li><svg class="tri" viewBox="0 0 18 18"><polygon points="9,1 17,17 1,17" fill="var(--green)"/></svg><span>Save Money</span></li>
    <li><svg class="tri" viewBox="0 0 18 18"><polygon points="9,1 17,17 1,17" fill="var(--green)"/></svg><span>Save Time</span></li>
    <li><svg class="tri" viewBox="0 0 18 18"><polygon points="9,1 17,17 1,17" fill="var(--green)"/></svg><span>Free Delivery, right to your door</span></li>
  </ul>
  <div class="abs gift">
    <svg viewBox="0 0 150 150" aria-hidden="true">
      <polygon fill="var(--green)" stroke="var(--white)" stroke-width="3" points="75,4 86,22 105,10 108,32 130,28 124,50 145,58 128,73 145,88 124,98 130,120 108,117 105,139 86,127 75,146 64,127 45,139 42,117 20,120 26,98 5,88 22,73 5,58 26,50 20,28 42,32 45,10 64,22"/>
    </svg>
    <div class="gift-text"><strong>$20</strong><span>GIFT CARD</span><span>is given with</span><span>your first</span><span>order</span></div>
  </div>
  <p class="abs offer-intro">We are a full service pharmacy that specializes in diabetic testing supplies and oral medications.</p>
  <ul class="abs offer-steps">
    <li>We are a full service pharmacy for diabetic testing. We research your insurance to determine how to save you the most money.</li>
    <li>We then contact your physician to get the appropriate authorization.</li>
    <li>We ship your testing supplies and oral medications directly to your home for free, every month.</li>
  </ul>
  <p class="abs offer-cta">Get started Today! Call our toll free number OR go to our website and fill our form.</p>
  <div class="abs brand offer-brand"><span class="brand-mark"></span><span class="brand-name">LINDEN<small>MEDICAL</small></span></div>
  <footer class="footer">
    <span class="contact"><svg viewBox="0 0 24 24"><path d="M6.6 10.8a15 15 0 0 0 6.6 6.6l2.2-2.2a1 1 0 0 1 1-.25 11.4 11.4 0 0 0 3.6.57 1 1 0 0 1 1 1V20a1 1 0 0 1-1 1A17 17 0 0 1 3 4a1 1 0 0 1 1-1h3.5a1 1 0 0 1 1 1c0 1.250.2 2.45.57 3.57a1 1 0 0 1-.25 1z"/></svg>800-555-0142</span>
    <span class="contact"><svg viewBox="0 0 24 24"><path d="M12 2a10 10 0 1 0 0 20 10 10 0 0 0 0-20zm0 2a8 8 0 0 1 0 16 8 8 0 0 1 0-16zM4 11h16v2H4zm7-7h2v16h-2z"/></svg>www.lindenmedical.com</span>
    <span class="contact"><svg viewBox="0 0 24 24"><path d="M2 5h20v14H2zm2 2v.5l8 5 8-5V7zm0 2.8V17h16V9.8l-8 5z"/></svg>lindenmed@mail.com</span>
  </footer>
</article>

<article class="flyer flyer--about">
  <div class="photo about-photo" role="img" aria-label="Photo of a smiling senior couple with a team of medical staff in scrubs behind them"></div>
  <div class="abs brand about-brand"><span class="brand-mark"></span><span class="brand-name">LINDEN<small>MEDICAL</small></span></div>
  <svg class="band" style="top:320px" height="120" viewBox="0 0 520 120" aria-hidden="true">
    <polygon points="0,0 380,70 520,92 520,120 0,120" fill="var(--white)"/>
    <polygon points="0,0 420,76 520,90 520,100 0,22" fill="var(--green)"/>
    <polygon points="0,22 520,100 520,112 0,44" fill="var(--grey-band)"/>
  </svg>
  <div class="abs free-badge"><span>COMPLETELY</span><strong>FREE!</strong></div>
  <h2 class="abs about-headline">We save the<br>patient, time and<br>money every month</h2>
  <p class="abs about-copy">We are a full service pharmacy that specializes in diabetic testing and medications. We research the patient's insurance to maximize their insurance benefit and then deliver the medications monthly directly to the patient's doorstep.</p>
  <div class="photo about-photo-a" role="img" aria-label="Photo of a pharmacist at shelves of medication"></div>
  <div class="photo about-photo-b" role="img" aria-label="Photo of hands using a blood glucose meter"></div>
  <footer class="footer">
    <span class="contact"><svg viewBox="0 0 24 24"><path d="M6.6 10.8a15 15 0 0 0 6.6 6.6l2.2-2.2a1 1 0 0 1 1-.25 11.4 11.4 0 0 0 3.6.57 1 1 0 0 1 1 1V20a1 1 0 0 1-1 1A17 17 0 0 1 3 4a1 1 0 0 1 1-1h3.5a1 1 0 0 1 1 1c0 1.250.2 2.45.57 3.57a1 1 0 0 1-.25 1z"/></svg>800-555-0142</span>
    <span class="contact"><svg viewBox="0 0 24 24"><path d="M12 2a10 10 0 1 0 0 20 10 10 0 0 0 0-20zm0 2a8 8 0 0 1 0 16 8 8 0 0 1 0-16zM4 11h16v2H4zm7-7h2v16h-2z"/></svg>www.lindenmedical.com</span>
    <span class="contact"><svg viewBox="0 0 24 24"><path d="M2 5h20v14H2zm2 2v.5l8 5 8-5V7zm0 2.8V17h16V9.8l-8 5z"/></svg>lindenmed@mail.com</span>
  </footer>
</article>

</body>
</html>
```